Granger Earthworks LLC business card design

Excavation company business cards

Contact Information for Business Card

Granger Earthworks LLC cell phone 208-555-0147 office phone 208-555-0193 grangerearthworksllc@mailnest.example Driveways, site prep, retaining walls, septic systems, rock delivery

Colors

Designer to choose colors to be used in the design.

```html
<!DOCTYPE html>
<html lang="en">
<head>
<meta charset="utf-8">
<title>Granger Earthworks LLC – Business Card</title>
<link rel="stylesheet" href="https://fonts.googleapis.com/css2?family=Montserrat:wght@400;500;800&display=swap">
<style>
  :root {
    --stage: #d9d9d9;
    --card-dark: #232323;
    --card-light: #ffffff;
    --edge: #e2641c;
    --orange: #ee6a1f;
    --ink: #4a4a4a;
    --emboss: #3b3b3b;
  }
  * { box-sizing: border-box; margin: 0; padding: 0; }
  html, body { width: 1200px; height: 801px; overflow: hidden; }
  body {
    background: var(--stage);
    font-family: "Montserrat", sans-serif;
    display: flex;
    align-items: center;
    justify-content: center;
    gap: 40px;
  }
  .card {
    position: relative;
    width: 540px;
    height: 309px;
    border-radius: 16px;
    border: 2px solid var(--edge);
    box-shadow: 0 8px 24px rgba(0,0,0,.18);
    overflow: hidden;
  }
  .card--back {
    background: var(--card-dark);
    display: flex;
    align-items: center;
    justify-content: center;
  }
  .back-brand {
    display: flex;
    align-items: center;
    gap: 10px;
    color: var(--emboss);
    font-weight: 800;
    font-size: 24px;
    letter-spacing: .5px;
    text-transform: uppercase;
    white-space: nowrap;
  }
  .back-brand .mark { width: 22px; height: 22px; background: var(--emboss); flex: none; }
  .card--front { background: var(--card-light); }
  .front-brand {
    position: absolute;
    top: 36px;
    right: 34px;
    display: flex;
    align-items: center;
    gap: 10px;
    color: var(--orange);
    font-weight: 800;
    font-size: 20px;
    text-transform: uppercase;
    letter-spacing: .5px;
    white-space: nowrap;
  }
  .front-brand .mark { width: 18px; height: 18px; background: var(--orange); flex: none; }
  .contact {
    position: absolute;
    right: 30px;
    top: 104px;
    list-style: none;
    color: var(--ink);
    font-size: 13px;
    font-weight: 500;
  }
  .contact li { display: flex; align-items: center; gap: 8px; margin-bottom: 8px; white-space: nowrap; }
  .contact svg { width: 14px; height: 14px; flex: none; }
  .person {
    position: absolute;
    left: 36px;
    bottom: 38px;
  }
  .person__name {
    color: var(--orange);
    font-weight: 800;
    font-size: 25px;
    letter-spacing: 1px;
    text-transform: uppercase;
    white-space: nowrap;
  }
  .person__role {
    color: var(--ink);
    font-size: 17px;
    font-weight: 400;
    margin-top: 2px;
  }
</style>
</head>
<body>
  <div class="card card--back">
    <div class="back-brand"><span class="mark"></span>Granger Earthworks LLC</div>
  </div>

  <div class="card card--front">
    <div class="front-brand"><span class="mark"></span>Granger Earthworks LLC</div>

    <ul class="contact">
      <li>
        <svg viewBox="0 0 14 14" aria-hidden="true"><rect x="3.5" y="1" width="7" height="12" rx="1.5" fill="none" stroke="#ee6a1f" stroke-width="1.4"/></svg>
        208-555-0147
      </li>
      <li>
        <svg viewBox="0 0 14 14" aria-hidden="true"><path d="M3 1.5l2.2 2.6-1.3 1.6c.9 1.9 2.4 3.4 4.3 4.3l1.6-1.3 2.6 2.2-1.5 1.8C6.4 12.5 1.5 7.6 1.2 3z" fill="#ee6a1f"/></svg>
        208-555-0193
      </li>
      <li>
        <svg viewBox="0 0 14 14" aria-hidden="true"><rect x="1" y="3" width="12" height="8.5" fill="#ee6a1f"/><path d="M1 3l6 5 6-5" fill="none" stroke="#fff" stroke-width="1.1"/></svg>
        grangerearthworksllc@mailnest.example
      </li>
    </ul>

    <div class="person">
      <p class="person__name">Dale Whitford</p>
      <p class="person__role">Excavator Operator</p>
    </div>
  </div>
</body>
</html>
```